Verelin Publishing

I made a website myself www.verelinpublishing.co.uk a few years ago but I need a new design, which I will code. One that I can be proud of, that 's sexy, to win new customers and showcase my publishing skills. This is a publishing website so I want the home page and books page to be fantastic. I have a logo already so will like the same colour scheme or thereabouts. I have current files and features that I would like to add to your creativity and experience.

Target Market(s)

Web Designers, Graphic Designers

Industry/Entity Type

Book Publisher

Number of Pages Required

5+ page

Font styles to use
Sans Serif

Colors
0255a3
ffffff
ec1f27

Requirements
Must have
• Menu and Sub Menu
• Footer
• Buy Page - Shopping Cart
• Upload feature on the submissions page
• video section on home page (how we publish books)
• Ad space section
Nice to have
• social media bar
• Zoom in page

```html
<!DOCTYPE html>
<html lang="en">
<head>
<meta charset="utf-8">
<title>Verelin Publishing — Self-Publishing That Works</title>
<link rel="stylesheet" href="https://fonts.googleapis.com/css2?family=Rubik:wght@400;500;700&family=Roboto:wght@300;400;500;700&display=swap">
<style>
:root{
  --navy:#1b1d4d;
  --blue:#0255a3;
  --red:#ec1f27;
  --green:#6cbd73;
  --green-card:#6bbf6f;
  --white:#ffffff;
  --ink:#222222;
  --muted:#7a7a7a;
  --grey-bg:#ececec;
  --head:"Rubik",Arial,sans-serif;
  --body:"Roboto",Arial,sans-serif;
}
*{box-sizing:border-box;margin:0;padding:0}
html,body{width:1200px;height:3896px;overflow:hidden}
body{font-family:var(--body);color:var(--ink);background:var(--white);position:relative}
section,header,footer{position:absolute;left:0;width:1200px}

/* Header & hero */
.hero{top:0;height:662px;background:linear-gradient(100deg,#d9cfc2 0%,#efe9e2 30%,#c9b7a3 55%,#6e5444 75%,#e7e4e2 100%)}
.site-nav{top:0;height:83px;background:rgba(27,29,77,.92);z-index:3}
.brand{position:absolute;left:78px;top:0;width:84px;height:96px;background:var(--white);display:flex;align-items:flex-end;justify-content:center;padding:0 4px 10px;box-shadow:0 2px 6px rgba(0,0,0,.2)}
.brand span{font-family:var(--head);font-weight:700;font-size:12px;color:var(--blue);text-align:center;line-height:1.1}
.brand::before{content:"";position:absolute;top:14px;left:27px;width:30px;height:30px;border-radius:50%;background:var(--red)}
.menu{position:absolute;left:232px;top:0;height:83px;display:flex;align-items:center;gap:37px;list-style:none}
.menu li{font-family:var(--head);font-weight:700;font-size:14px;color:var(--white);letter-spacing:.3px}
.nav-tools{position:absolute;right:80px;top:28px;display:flex;gap:24px}
.hero-title{position:absolute;left:330px;top:286px;width:540px;text-align:center;z-index:2}
.hero-title h1{font-family:var(--head);font-weight:700;font-size:46px;line-height:1.05;color:var(--blue)}
.hero-title p{font-family:var(--head);font-weight:500;font-size:30px;line-height:1.2;color:var(--blue);border-top:3px solid var(--blue);border-bottom:3px solid var(--blue);margin-top:4px;padding:2px 0}
.btn-red{position:absolute;left:510px;top:440px;width:180px;height:48px;background:var(--red);color:var(--white);font-family:var(--head);font-weight:700;font-size:16px;display:flex;align-items:center;justify-content:center}
.slider-dots{position:absolute;left:550px;top:615px;display:flex;gap:6px}
.slider-dots i{width:16px;height:16px;border-radius:50%;border:2px solid var(--blue);background:var(--white)}
.slider-dots i.on{background:var(--blue)}

/* Intro */
.intro{top:662px;height:280px;text-align:center}
.intro h2{font-family:var(--body);font-weight:500;font-size:34px;margin-top:65px;color:#111}
.intro .rule{width:155px;height:3px;background:var(--blue);margin:14px auto 0;opacity:.7}
.intro p{width:790px;margin:26px auto 0;font-family:var(--body);font-weight:300;font-size:23px;line-height:1.45;color:var(--muted)}

/* Feature cards */
.features{top:935px;height:433px;background:var(--grey-bg)}
.features .notch{position:absolute;top:0;left:0}
.cards{position:absolute;left:112px;top:125px;display:flex;gap:21px}
.card{width:311px;height:246px;position:relative;color:var(--white);display:flex;flex-direction:column;align-items:center;justify-content:flex-end;padding-bottom:48px}
.card::after{content:"";position:absolute;inset:10px;border:1px dashed rgba(255,255,255,.6)}
.card.books{background:var(--green-card)}
.card.authors{background:var(--blue)}
.card.submissions{background:var(--red)}
.card svg{margin-bottom:22px}
.card h3{font-family:var(--head);font-weight:500;font-size:25px}

/* Video */
.video{top:1368px;height:462px;background:linear-gradient(90deg,#4a3c36 0%,#6d5a50 40%,#3d342f 60%,#5a4a42 100%)}
.video::before{content:"";position:absolute;inset:0;background:rgba(0,0,0,.35)}
.video h2{position:absolute;top:122px;width:100%;text-align:center;font-family:var(--head);font-weight:700;font-size:41px;color:var(--white)}
.video .play{position:absolute;left:548px;top:213px}

/* Steps */
.steps{top:1830px;height:551px;text-align:center}
.steps h2{font-family:var(--head);font-weight:500;font-size:41px;margin-top:60px;color:#111}
.step-row{position:absolute;left:74px;top:168px;width:1052px;display:flex}
.step-row::before{content:"";position:absolute;left:0;right:0;top:140px;height:2px;background:#f2a6a8}
.step{flex:1;position:relative;display:flex;flex-direction:column;align-items:center}
.step .num{position:absolute;top:88px;font-family:var(--head);font-weight:700;font-size:110px;color:#efefef;line-height:1}
.step h3{position:relative;z-index:1;margin-top:66px;background:var(--white);padding:0 10px;font-family:var(--head);font-weight:500;font-size:26px;color:#111}
.step p{position:relative;width:235px;margin-top:36px;font-size:13.5px;line-height:1.6;color:#333}

/* Partners */
.partners{top:2381px;height:325px;background:var(--green)}
.partners h2{text-align:center;font-family:var(--head);font-weight:500;font-size:35px;color:var(--white);margin-top:66px}
.partner-row{position:absolute;left:93px;top:154px;display:flex;gap:19px}
.partner{width:153px;height:98px;background:var(--white);display:flex;align-items:center;justify-content:center;font-family:var(--body);font-weight:500;font-size:21px;color:#333;text-align:center;line-height:1.1}

/* Our work */
.work{top:2706px;height:553px;background:repeating-linear-gradient(0deg,#2a2a2c 0 38px,#1f1f21 38px 41px)}
.work-panel{position:absolute;left:73px;top:107px;width:1051px;height:363px;background:var(--white);border-radius:10px}
.work-tab{position:absolute;left:420px;top:-16px;width:360px;height:54px;background:var(--white);border-radius:8px 8px 0 0;display:flex;align-items:center;justify-content:center;font-family:var(--head);font-weight:500;font-size:34px;color:#111}
.covers{position:absolute;left:75px;top:90px;width:900px;display:flex;justify-content:space-between}
.cover{width:150px;height:226px;box-shadow:0 3px 8px rgba(0,0,0,.3)}
.cover.c1{background:linear-gradient(180deg,#e7d7b5,#6c7a3e)}
.cover.c2{background:linear-gradient(180deg,#262626,#0d0d0d)}
.cover.c3{background:linear-gradient(180deg,#1d3b8a,#d49a3a)}
.cover.c4{background:linear-gradient(180deg,#a8202a,#7a1119)}

/* Testimonials */
.testimonials{top:3259px;height:411px}
.testimonials h2{position:absolute;left:91px;top:60px;font-family:var(--head);font-weight:500;font-size:36px;color:#111}
.quote-box{position:absolute;left:91px;top:125px;width:735px;height:218px;background:#ebebe6}
.avatar{position:absolute;left:43px;top:50px;width:130px;height:130px;border-radius:50%;background:linear-gradient(160deg,#8fa3b0,#c9a68d)}
.quote-box blockquote{position:absolute;left:210px;top:70px;width:470px;font-size:21px;line-height:1.4;color:#555}
.qnav{position:absolute;top:101px;width:26px;height:26px;background:#444;display:flex;align-items:center;justify-content:center}
.ad{position:absolute;left:849px;top:65px;width:278px;height:281px;background:linear-gradient(135deg,#f2f2f2,#e3e3e3)}
.ad .watch{position:absolute;left:0;top:0;width:120px;height:281px;background:linear-gradient(180deg,#7a1a12,#b04a2a,#6e1a12)}
.ad .copy{position:absolute;right:22px;top:18px;text-align:right;font-family:var(--head);color:#222}
.ad .copy small{display:block;font-size:12px;letter-spacing:2px}
.ad .copy strong{display:block;font-weight:700;font-size:24px;line-height:1}
.ad .brandname{position:absolute;right:40px;top:132px;font-family:var(--head);font-weight:700;font-size:20px;color:#222}
.ad .shop{position:absolute;right:22px;top:212px;width:110px;height:24px;background:#1c6c96;color:#fff;font-family:var(--head);font-size:12px;display:flex;align-items:center;justify-content:center}
.ad .url{position:absolute;right:22px;top:248px;font-size:10px;color:#555}

/* Footer */
.site-footer{top:3670px;height:226px;background:var(--navy);color:var(--white)}
.footer-brand{position:absolute;left:182px;top:13px;width:130px;height:178px;background:var(--white);display:flex;align-items:flex-end;justify-content:center;padding-bottom:18px;clip-path:polygon(0 0,100% 0,100% 92%,50% 100%,0 92%)}
.footer-brand::before{content:"";position:absolute;top:30px;left:40px;width:50px;height:50px;border-radius:50%;background:var(--red)}
.footer-brand span{font-family:var(--head);font-weight:700;font-size:17px;color:var(--blue);text-align:center;line-height:1.1}
.footer-links{position:absolute;top:64px;list-style:none;font-size:15px;line-height:1.7}
.social{position:absolute;left:748px;top:58px}
.social h4{font-family:var(--head);font-weight:700;font-size:12px;margin-bottom:12px}
.social div{display:flex;gap:4px}
.social i{width:32px;height:32px;display:block}
.copyright{position:absolute;bottom:6px;width:100%;text-align:center;font-size:11px;color:#c7c8d8;border-top:1px solid rgba(255,255,255,.15);padding-top:6px;left:0}
</style>
</head>
<body>

<section class="hero" role="img" aria-label="Photo of a smiling woman working on a laptop">
  <div class="hero-title">
    <h1>VERELIN PUBLISHING</h1>
    <p>SELF-PUBLISHING THAT WORKS</p>
  </div>
  <a class="btn-red">SUBMIT BOOK</a>
  <div class="slider-dots"><i class="on"></i><i></i><i></i><i></i><i></i></div>
</section>

<header class="site-nav">
  <div class="brand"><span>Verelin Publishing</span></div>
  <ul class="menu">
    <li>HOME</li><li>PUBLISHING</li><li>SUBMISSIONS</li><li>BOOKS</li><li>AUTHORS</li><li>SEMINARS</li><li>CONTACT</li>
  </ul>
  <div class="nav-tools">
    <svg width="24" height="24" viewBox="0 0 24 24" fill="none" stroke="#fff" stroke-width="2"><circle cx="10" cy="10" r="7"/><line x1="15" y1="15" x2="22" y2="22"/></svg>
    <svg width="22" height="24" viewBox="0 0 22 24" fill="none" stroke="#fff" stroke-width="2"><rect x="2" y="7" width="18" height="15"/><path d="M7 10V5a4 4 0 0 1 8 0v5"/></svg>
  </div>
</header>

<section class="intro">
  <h2>Have a story to tell? We can help you publish your book.</h2>
  <div class="rule"></div>
  <p>Welcome to Verelin Publishing, we are an independent publishing company located in London/Surrey. We publish Trade (fiction and non-fiction), &amp; Young Adult (YA) in a variety of subjects.</p>
</section>

<section class="features">
  <svg class="notch" width="1200" height="100" viewBox="0 0 1200 100"><polygon points="0,0 1200,0 1200,20 600,90 0,20" fill="#fff"/></svg>
  <div class="cards">
    <div class="card books">
      <svg width="80" height="66" viewBox="0 0 80 66" fill="none" stroke="#fff" stroke-width="4"><rect x="8" y="4" width="64" height="16" rx="3"/><rect x="4" y="24" width="64" height="16" rx="3"/><rect x="10" y="44" width="64" height="16" rx="3"/></svg>
      <h3>BOOKS</h3>
    </div>
    <div class="card authors">
      <svg width="66" height="70" viewBox="0 0 66 70" fill="#fff"><circle cx="33" cy="18" r="16"/><path d="M2 70c0-20 14-32 31-32s31 12 31 32z"/></svg>
      <h3>AUTHORS</h3>
    </div>
    <div class="card submissions">
      <svg width="76" height="66" viewBox="0 0 76 66" fill="#fff"><path d="M4 20h20v8H12v30h44v-8h8v16H4z"/><path d="M46 4l26 20-26 20V32c-12 0-20 4-26 12 2-16 10-26 26-28z"/></svg>
      <h3>SUBMISSIONS</h3>
    </div>
  </div>
</section>

<section class="video" role="img" aria-label="Video still of two women talking in a bookshop">
  <h2>LEARN HOW WE PUBLISH BOOKS</h2>
  <svg class="play" width="104" height="104" viewBox="0 0 104 104"><circle cx="52" cy="52" r="46" fill="none" stroke="#fff" stroke-width="7"/><polygon points="42,32 72,52 42,72" fill="#fff"/></svg>
</section>

<section class="steps">
  <h2>PUBLISH YOUR BOOK IN 4 EASY STEPS</h2>
  <div class="step-row">
    <div class="step">
      <svg width="60" height="60" viewBox="0 0 60 60" fill="none" stroke="#0255a3" stroke-width="2.5"><path d="M12 48l4-12 28-28 8 8-28 28z"/><line x1="38" y1="14" x2="46" y2="22"/></svg>
      <div class="num">1.</div><h3>WRITING</h3>
      <p>You write a book to the best of your ability and after redrafting it several times, when you feel it is ready, send it to us.</p>
    </div>
    <div class="step">
      <svg width="60" height="60" viewBox="0 0 60 60" fill="none" stroke="#0255a3" stroke-width="2.5"><path d="M16 6h20l10 10v38H16z"/><path d="M36 6v10h10"/><path d="M31 42V26m-6 6l6-6 6 6"/></svg>
      <div class="num">2.</div><h3>SUBMISSION</h3>
      <p>If your book is in our subject matter and you think it could catch our eye, send us your book for review.</p>
    </div>
    <div class="step">
      <svg width="60" height="60" viewBox="0 0 60 60" fill="none" stroke="#0255a3" stroke-width="2.5"><polygon points="30,6 37,22 54,23 41,34 45,51 30,42 15,51 19,34 6,23 23,22"/></svg>
      <div class="num">3.</div><h3>REVIEW</h3>
      <p>You send us your book and our editorial team will look over it and decide if we like it.</p>
    </div>
    <div class="step">
      <svg width="60" height="60" viewBox="0 0 60 60" fill="none" stroke="#0255a3" stroke-width="2.5"><rect x="12" y="10" width="36" height="44" rx="2"/><rect x="22" y="6" width="16" height="8"/><line x1="20" y1="26" x2="40" y2="26"/><line x1="20" y1="34" x2="40" y2="34"/><line x1="20" y1="42" x2="32" y2="42"/></svg>
      <div class="num">4.</div><h3>CONTRACT</h3>
      <p>You send us your book and our editorial team will decide if we like it, and then we will agree terms.</p>
    </div>
  </div>
</section>

<section class="partners">
  <h2>COMPANIES WE WORK WITH</h2>
  <div class="partner-row">
    <div class="partner">Northshelf</div>
    <div class="partner">Readwell</div>
    <div class="partner">Pressly</div>
    <div class="partner">PageTree</div>
    <div class="partner">Harbor &amp; Finch</div>
    <div class="partner">Leafnook</div>
  </div>
</section>

<section class="work">
  <div class="work-panel">
    <div class="work-tab">OUR WORK</div>
    <div class="covers">
      <div class="cover c1" role="img" aria-label="Book cover with a collage of lifestyle photos"></div>
      <div class="cover c2" role="img" aria-label="Book cover with white title type on black"></div>
      <div class="cover c3" role="img" aria-label="Book cover with an illustrated desert scene"></div>
      <div class="cover c4" role="img" aria-label="Book cover with a red patterned design"></div>
    </div>
  </div>
  <svg style="position:absolute;left:60px;top:242px" width="30" height="30" viewBox="0 0 30 30"><circle cx="15" cy="15" r="13" fill="#fff" stroke="#555" stroke-width="2"/><polyline points="17,9 11,15 17,21" fill="none" stroke="#555" stroke-width="2.5"/></svg>
  <svg style="position:absolute;left:1108px;top:242px" width="30" height="30" viewBox="0 0 30 30"><circle cx="15" cy="15" r="13" fill="#fff" stroke="#555" stroke-width="2"/><polyline points="13,9 19,15 13,21" fill="none" stroke="#555" stroke-width="2.5"/></svg>
</section>

<section class="testimonials">
  <h2>TESTIMONIALS</h2>
  <div class="quote-box">
    <div class="qnav" style="left:-13px"><svg width="10" height="12" viewBox="0 0 10 12"><polygon points="8,0 0,6 8,12" fill="#fff"/></svg></div>
    <div class="avatar" role="img" aria-label="Portrait of the reviewing author"></div>
    <blockquote>"You send us your book and our editorial team will look over it and decide if we like it and then we will Decide what."</blockquote>
    <div class="qnav" style="right:-13px"><svg width="10" height="12" viewBox="0 0 10 12"><polygon points="2,0 10,6 2,12" fill="#fff"/></svg></div>
  </div>
  <aside class="ad" aria-label="Advertisement">
    <div class="watch" role="img" aria-label="Product photo of a red wooden wristwatch"></div>
    <div class="copy"><small>LUXURY</small><strong>WOOD<br>WATCHES</strong></div>
    <div class="brandname">Tallow</div>
    <div class="shop">SHOP NOW</div>
    <div class="url">TALLOWTIME.COM</div>
  </aside>
</section>

<footer class="site-footer">
  <div class="footer-brand"><span>Verelin Publishing</span></div>
  <ul class="footer-links" style="left:353px"><li>Submissions</li><li>Production</li><li>Ebooks</li></ul>
  <ul class="footer-links" style="left:506px"><li>Books</li><li>Seminars</li><li>Packages</li></ul>
  <ul class="footer-links" style="left:634px"><li>Authors</li><li>Contact</li><li>Career</li></ul>
  <div class="social">
    <h4>STAY CONNECTED</h4>
    <div><i style="background:#3b5998"></i><i style="background:#29a9e1"></i><i style="background:#d34836"></i><i style="background:#0e76a8"></i><i style="background:#cb2027"></i></div>
  </div>
  <div class="copyright">© 2016 Verelin Publishing. All Rights Reserved.</div>
</footer>

</body>
</html>
```